Tilly the Otter - Kids (2-5years) - ALL NATURAL - Bath & Body Skincare - Label / Packaging Design

Carnwick Heather Estate is the owner of the 'celebrity' lavender bear, Tilly the Otter. Carnwick is the world largest commercial lavender farm and home to the world finest lavender, lavender oil and skincare products. www.carnwickheather-example.com

We are launching a line of Kids skincare products targeted to the Australian and China market (where Tilly is considered a superstar/celebrity).

All natural products made in Australia:

We are looking for 3-4 few packaging concept designs for packaging for our Tilly Kids - Bath, Body & Bed Range.

The "Tilly Kids" Toiletry Range includes:
= Shampoo/Bath Gel
= Fizzy Bath Bombs
= Moisturiser
= Pillow Spray (together aka the “Tilly Snoozetime Routine”)

= Later, possible additions to the Tilly the Otter range include the below items so the conceptual design must be adaptable.
- Bath robe
- Bed Linen Sets
- Crockey sets

See Filecrate folder here for all image and brand information:
https://www.filecrate-example.com/sh/8kqmvr2tw9x3hn1/QQpzrLmeTdFgYh7kWsVuXcA2b?dl=0

Note: There are some current DRAFT concept created by another designer in the image section of the brief. These are NOT ready or high quality enough (and too dull and busy) but will give you a good reference for what we don't want (too dark/busy/illegible). Please create new ideas....
Updates

HI - NEW FILECRATE FILE LINK IN CASE THE ONE I SENT PREVIOUSLY IS NOT WORKING - https://www.filecrate-example.com/sh/8kqmvr2tw9x3hn1/QQpzrLmeTdFgYh7kWsVuXcA2b?dl=0IVE ALSO ADDED A FEW NEW FILES... Added Wednesday, June 14, 2017

Pls see links to Penrick's and TOTs Organic... http://www.boxdesignshowcase-example.com/2017/02/tots-organic.html https://www.penricksorganic-example.com.au We asked our social media agency in china for their thoughts on the colour scheme's so far (not including new attempts here) and they said the following: "From our perspective - we agree that the colour hues are not quite right - and while we love Tilly, we wonder whether the current design and packaging options doesn't quite reflect the premium price points that you want to position these products. We are aware that you are limited with a certain number of packaging options but worry that the pale and purple colours may not attract Chinese parents. While sunscreen is not a premium product - please see the Chasing Wren package that one of our clients has had strong sales in China https://www.sunsafeshop-example.org.au/product/wren-splash-play-sunscreen.html In short, the Tilly design needs to be colourful, rich and vibrant in our opinion"

Target Market(s)

Children 2-5 years old. Primarily young Australian and Chinese mothers and their children.

Industry/Entity Type

Farm

Font styles to use
Other font styles liked:
• Topik px is the main wordmark font. The copy font is your choice.

Requirements
Must have
• Specifically, a general Packaging Design that can be used across a wide range of products and packaging types.
• Packaging & Visual Design –Important Considerations:
• Please be creative!
• •Please ensure the design can be used as a (waterproof) label or printed on the bottle...
• • Please show the design on various bottle sizes and colours (clear, white, cream etc)
• • Please suggest various eco-friendly bottle material (PBS free recyclable plastic)?
• • Must have multi-country / cultural appeal
• Must be polished, fun, western/australian design standard but also appeals to Chinese design tastes..
• Feel free to add some splashes of kid-friendly colours - blues, pinks, yellow, greens etc
• See Filecrate folder here for all image and brand information:
• https://www.filecrate-example.com/sh/8kqmvr2tw9x3hn1/QQpzrLmeTdFgYh7kWsVuXcA2b?dl=0
• Notes from our contracts manufacturer:
• "For the tube there will be limitation to the puck size, this is the opening diameter of the tube. On the tube you are not able to print 6mm from the top of the tube closure when printing. For sticker application on the tube you will need to allow for spacing on each edge to ensure there is no creasing"
• The current budget covers the overall concept and (and 1 x packaging completed) We are willing to negotiate an additional small cost for the extra 2-3 product specific designs.
• We expect print ready packaging and we will supply the dielines to the chosen designer once we have decided upon the exact size, style and approach for the packaging - printing or labels (this part might take a few weeks as we need to review our options) but we can release (part) payment before if required.
Should not have
• No brown-bottles please.

```html
<!DOCTYPE html>
<html lang="en">
<head>
<meta charset="utf-8">
<title>Tilly Kids – Bath, Body &amp; Bed Range labels</title>
<link href="https://fonts.googleapis.com/css2?family=Delius&family=Gochi+Hand&display=swap" rel="stylesheet">
<style>
  :root {
    --page: #ececec;
    --ink: #1d1d1b;
    --white: #ffffff;
    --blue-tint: #d5ebf6;
    --blue-cloud: #8ccbea;
    --blue-strong: #1b9ad8;
    --pink-tint: #efdcee;
    --pink-cloud: #e5a9d0;
    --pink-strong: #e35fae;
    --green-tint: #d3e9dd;
    --green-cloud: #9ecbae;
    --green-strong: #2ca46c;
    --art-warm: #f6e7a8;
  }
  * { box-sizing: border-box; margin: 0; padding: 0; }
  html, body { width: 1200px; height: 880px; overflow: hidden; }
  body { background: var(--page); font-family: "Delius", cursive; color: var(--ink); position: relative; }

  .label {
    position: absolute; top: 90px; width: 320px; height: 700px;
    border-radius: 28px; overflow: hidden; background: var(--tint);
  }
  .label--gel { left: 60px; --tint: var(--blue-tint); --cloud: var(--blue-cloud); --strong: var(--blue-strong); }
  .label--cream { left: 440px; --tint: var(--pink-tint); --cloud: var(--pink-cloud); --strong: var(--pink-strong); }
  .label--spray { left: 820px; --tint: var(--green-tint); --cloud: var(--green-cloud); --strong: var(--green-strong); }

  .cloud-band { position: absolute; inset: 0; width: 320px; height: 700px; }
  .cloud-band path { fill: var(--cloud); }

  .wordmark {
    position: absolute; top: 282px; left: 0; width: 100%; text-align: center;
    font-family: "Delius", cursive; font-size: 44px; letter-spacing: 1px;
    color: var(--ink); text-transform: uppercase;
  }
  .range-line {
    position: absolute; top: 346px; left: 0; width: 100%; text-align: center;
    font-size: 20px; color: var(--ink);
  }
  .bubbles { position: absolute; left: 0; top: 380px; width: 320px; height: 120px; }
  .bubbles .ring-strong { fill: none; stroke: var(--strong); stroke-width: 6; }
  .bubbles .ring-light { fill: none; stroke: var(--white); stroke-width: 2; }
  .bubbles .dot { fill: var(--strong); }

  .character-art {
    position: absolute; left: 120px; top: 392px; width: 180px; height: 190px;
    border-radius: 40px;
    background: radial-gradient(circle at 45% 35%, var(--white) 0 45%, var(--art-warm) 100%);
  }
  .volume {
    position: absolute; left: 26px; top: 492px; font-size: 22px;
    color: var(--ink); transform: rotate(-32deg); transform-origin: left center;
  }
  .product-name {
    position: absolute; left: 50px; top: 545px; width: 112px; height: 112px;
    border-radius: 50%; background: var(--strong); color: var(--white);
    display: flex; align-items: center; justify-content: center; text-align: center;
    font-family: "Gochi Hand", cursive; font-size: 28px; line-height: 0.95;
  }
</style>
</head>
<body>

<section class="label label--gel">
  <svg class="cloud-band" viewBox="0 0 320 700" aria-hidden="true">
    <path d="M0 250 C0 195 55 185 85 212 C95 150 210 140 228 200 C255 168 320 178 320 228 L320 700 L0 700 Z"/>
  </svg>
  <h2 class="wordmark">Tilly Kids</h2>
  <p class="range-line">Bath, Body &amp; Bed Range</p>
  <svg class="bubbles" viewBox="0 0 320 120" aria-hidden="true">
    <circle class="ring-strong" cx="44" cy="40" r="26"/>
    <circle class="ring-light" cx="54" cy="32" r="20"/>
    <circle class="dot" cx="290" cy="18" r="4"/>
  </svg>
  <div class="character-art" role="img" aria-label="Illustration of a white reindeer character with a stitched yellow-outlined body"></div>
  <span class="volume">500ml</span>
  <div class="product-name">shower<br>gel</div>
</section>

<section class="label label--cream">
  <svg class="cloud-band" viewBox="0 0 320 700" aria-hidden="true">
    <path d="M0 250 C0 195 55 185 85 212 C95 150 210 140 228 200 C255 168 320 178 320 228 L320 700 L0 700 Z"/>
  </svg>
  <h2 class="wordmark">Tilly Kids</h2>
  <p class="range-line">Bath, Body &amp; Bed Range</p>
  <svg class="bubbles" viewBox="0 0 320 120" aria-hidden="true">
    <circle class="ring-strong" cx="44" cy="40" r="26"/>
    <circle class="ring-light" cx="54" cy="32" r="20"/>
    <circle class="dot" cx="290" cy="18" r="4"/>
  </svg>
  <div class="character-art" role="img" aria-label="Illustration of a penguin character with a stitched yellow-outlined body"></div>
  <span class="volume">500ml</span>
  <div class="product-name">moisture<br>cream</div>
</section>

<section class="label label--spray">
  <svg class="cloud-band" viewBox="0 0 320 700" aria-hidden="true">
    <path d="M0 250 C0 195 55 185 85 212 C95 150 210 140 228 200 C255 168 320 178 320 228 L320 700 L0 700 Z"/>
  </svg>
  <h2 class="wordmark">Tilly Kids</h2>
  <p class="range-line">Bath, Body &amp; Bed Range</p>
  <svg class="bubbles" viewBox="0 0 320 120" aria-hidden="true">
    <circle class="ring-strong" cx="44" cy="40" r="26"/>
    <circle class="ring-light" cx="54" cy="32" r="20"/>
  </svg>
  <div class="character-art" role="img" aria-label="Illustration of a white seal pup character with a stitched yellow-outlined body"></div>
  <span class="volume">500ml</span>
  <div class="product-name">pillow<br>spray</div>
</section>

</body>
</html>
```